Long Established Local Fencing (not swords) Business needs fresh Business Cards

We need fresh double sided business cards for our Fencing Construction business, we are looking for something with our new logo design added, and maybe a photo background ?
We recently had cards made from Quillmarko and we were horrified with what we got back, the quality was terrible, so am looking for high quality format for good printing company to make.
We install Steelwave, Timber paling, Aluminium Slat Screening, Picket (timber and aluminium) and most other fencing installations.
Our website is brelbanfencing.com.au should you like to learn a bit more.
We do have logo in other formats if required.
We have been in business for over 35 years and we have used this as a "motto" it is on our signage

Industry/Entity Type

Construction

Contact Information for Business Card

Open to ideas, we need 3 x different cards, one generic with no name and 2 x others each with 1 of our bosses name on each, I will put into upload files.

Colors
ec1f27
000000
606060
f5f5f5

Requirements
Must have
• Company Name and Logo
• Address
• Contact details, phone, website, email etc
• Small space to write notes when leaving card at residence
Nice to have
• Our motto "Servicing the Peninsula for over 35 years"

```html
<!DOCTYPE html>
<html lang="en">
<head>
<meta charset="utf-8">
<title>Brelban Fencing – Business Cards</title>
<link href="https://fonts.googleapis.com/css2?family=Lato:wght@400;700;900&display=swap" rel="stylesheet">
<style>
  :root {
    --red: #ec1f27;
    --black: #111111;
    --grey: #5f6366;
    --paper: #f5f5f5;
    --backdrop: #cfd3d4;
    --rule: #8a8a8a;
    --white: #ffffff;
  }
  * { box-sizing: border-box; margin: 0; padding: 0; }
  html, body { width: 1200px; height: 1050px; overflow: hidden; }
  body {
    background: var(--backdrop);
    font-family: "Lato", sans-serif;
    display: flex;
    flex-direction: column;
    align-items: center;
    justify-content: center;
    gap: 60px;
  }
  .card {
    width: 760px;
    height: 434px;
    position: relative;
    box-shadow: 0 10px 30px rgba(0,0,0,0.12);
  }
  /* Back side */
  .card-back {
    background: var(--grey);
    display: flex;
    flex-direction: column;
    align-items: center;
    justify-content: center;
    gap: 26px;
    color: var(--white);
  }
  .brand {
    display: flex;
    align-items: center;
    gap: 16px;
  }
  .brand-dot {
    width: 22px; height: 22px;
    border-radius: 50%;
    background: var(--red);
    flex: none;
  }
  .brand-name {
    font-weight: 900;
    letter-spacing: 3px;
    text-transform: uppercase;
    white-space: nowrap;
  }
  .card-back .brand-name { font-size: 50px; color: var(--white); }
  .motto { font-size: 21px; font-weight: 400; letter-spacing: 0.3px; }
  .motto strong { font-weight: 900; }

  /* Front side */
  .card-front {
    background: var(--paper);
    color: var(--black);
    padding: 54px 60px;
  }
  .person-name { font-size: 30px; font-weight: 700; }
  .person-role { font-size: 21px; color: var(--red); margin-top: 4px; }
  .divider {
    position: absolute;
    left: 60px; right: 60px; top: 150px;
    height: 1px;
    background: var(--rule);
  }
  .contacts {
    list-style: none;
    position: absolute;
    left: 60px; top: 176px;
    display: flex; flex-direction: column; gap: 12px;
    font-size: 21px;
  }
  .contacts li { display: flex; align-items: center; gap: 14px; white-space: nowrap; }
  .contacts svg { width: 18px; height: 18px; flex: none; }
  .card-front .brand {
    position: absolute;
    right: 60px; top: 72px;
    gap: 12px;
  }
  .card-front .brand-name { font-size: 28px; color: var(--black); }
  .card-front .brand-dot { width: 16px; height: 16px; }
  .address {
    position: absolute;
    right: 60px; bottom: 50px;
    text-align: right;
    font-style: normal;
    font-size: 21px;
    line-height: 1.35;
  }
</style>
</head>
<body>

<section class="card card-back" aria-label="Card back">
  <div class="brand">
    <span class="brand-dot"></span>
    <span class="brand-name">Brelban Fencing</span>
  </div>
  <p class="motto">Servicing the Peninsula for <strong>over 35 years</strong></p>
</section>

<section class="card card-front" aria-label="Card front">
  <h1 class="person-name">Daniel Hartley</h1>
  <p class="person-role">Managing Director</p>

  <div class="brand">
    <span class="brand-dot"></span>
    <span class="brand-name">Brelban Fencing</span>
  </div>

  <div class="divider"></div>

  <ul class="contacts">
    <li>
      <svg viewBox="0 0 24 24" aria-hidden="true"><path d="M6.6 10.8a15.1 15.1 0 0 0 6.6 6.6l2.2-2.2a1 1 0 0 1 1-.25 11.4 11.4 0 0 0 3.6.57 1 1 0 0 1 1 1V20a1 1 0 0 1-1 1A17 17 0 0 1 3 4a1 1 0 0 1 1-1h3.5a1 1 0 0 1 1 1c0 1.25.2 2.45.57 3.57a1 1 0 0 1-.25 1z" fill="var(--red)"/></svg>
      02 4000 5812
    </li>
    <li>
      <svg viewBox="0 0 24 24" aria-hidden="true"><rect x="2.5" y="5" width="19" height="14" fill="none" stroke="var(--red)" stroke-width="1.8"/><path d="M2.5 5l9.5 8 9.5-8" fill="none" stroke="var(--red)" stroke-width="1.8"/></svg>
      brelbanfencing@mailpond.com
    </li>
    <li>
      <svg viewBox="0 0 24 24" aria-hidden="true"><circle cx="12" cy="12" r="9.5" fill="none" stroke="var(--red)" stroke-width="1.8"/><ellipse cx="12" cy="12" rx="4" ry="9.5" fill="none" stroke="var(--red)" stroke-width="1.5"/><path d="M2.5 12h19M4 7h16M4 17h16" stroke="var(--red)" stroke-width="1.3"/></svg>
      www.brelbanfencing.com.au
    </li>
  </ul>

  <address class="address">
    42 Tern Street<br>
    Brelban<br>
    Nsw 2299
  </address>
</section>

</body>
</html>
```